Creative Web Design - Intl Market Research Company

We need an innovative web design for an emerging company into the international market research marketplace.

The company, Halvenor Associates, is a Trade, Investment, and Market Research company. Halvenor offers domestic and international companies increased success in the U.S. marketplace by providing a variety of services. (seen on attached brochure)

The website should be cutting edge and creative while having an easy navigation. The color is not fixed and attached logo is not finalized, feel free to post anything from conservative to progressive options. Keep in mind target customers are domestic and international businesses looking to emerge/improve in the U.S. marketplace.

Additional Company information is located in the attached documentation. The documentation is outdated & winner will have priority standing for our next projects.(logo & document re-design)

I have received a few e-mail requests and have updated the status to guaranteed payment.

Thanks!

Target Market(s)

Any company, foreign and domestic, looking to introduce their product into the U.S. marketplace.

Industry/Entity Type

Market Research

Requirements
Must have
• Easy Navigation
Should not have
• Too many buttons
Difficult navigation
Excessive Typography

```html
<!DOCTYPE html>
<html lang="en">
<head>
<meta charset="utf-8">
<title>Halvenor Associates</title>
<link rel="stylesheet" href="https://fonts.googleapis.com/css2?family=Open+Sans:wght@400;600;700&family=Questrial&family=Raleway:wght@400;500&display=swap">
<style>
:root{
  --blue:#2a8fd6;
  --blue-deep:#1a6fb8;
  --band:#5fb6e4;
  --top-blue:#2f7fcf;
  --nav-bg:#1b1c1e;
  --orange:#f26a10;
  --green:#5db82e;
  --ink:#555a60;
  --muted:#8a9097;
  --footer:#1e2124;
  --footer-text:#8d9399;
  --white:#ffffff;
  --line:#dfe3e7;
}
*{box-sizing:border-box;margin:0;padding:0}
html,body{width:882px;height:1200px;overflow:hidden;background:var(--white)}
body{position:relative;font-family:"Open Sans",Arial,sans-serif;color:var(--ink)}
.topbar{position:absolute;top:0;left:0;width:882px;height:18px;background:linear-gradient(#3a8ee0,#236ec0);color:var(--white);font-size:8px;line-height:18px;padding-left:148px}
.topbar .dot{display:inline-block;width:9px;height:9px;border-radius:50%;background:var(--white);vertical-align:-1px;margin-right:4px}
.topbar b{font-weight:600}
.site-nav{position:absolute;top:18px;left:0;width:882px;height:54px;background:var(--nav-bg)}
.menu{position:absolute;right:131px;top:19px;display:flex;gap:11px;align-items:center;font-size:8.5px;font-weight:600;color:var(--white)}
.btn-sm{display:inline-block;padding:4px 5px;border-radius:2px;color:var(--white);font-size:8.5px}
.btn-signup{background:var(--orange)}
.btn-login{background:var(--green)}
.hero{position:absolute;top:72px;left:0;width:882px;height:330px;overflow:hidden}
.hero-photo{position:absolute;inset:0;background:linear-gradient(100deg,#8c8f8e 0%,#b7b4ab 30%,#6c6a66 55%,#a9aca8 75%,#7d807f 100%)}
.hero-copy{position:absolute;left:147px;top:94px;color:var(--white)}
.hero-copy h1{font-family:"Raleway",sans-serif;font-weight:500;font-size:24px;letter-spacing:.2px}
.hero-copy p{font-family:"Raleway",sans-serif;font-size:13.5px;line-height:17px;margin:4px 0 0 4px;width:270px}
.cta{position:absolute;left:146px;top:174px;width:151px;height:34px;background:var(--blue);color:var(--white);font-family:"Raleway",sans-serif;font-weight:500;font-size:11px;line-height:34px;text-align:center;border-radius:1px}
.arrow{position:absolute;top:128px}
.hero-edge{position:absolute;left:0;bottom:0}
.intro{position:absolute;top:414px;left:0;width:882px;text-align:center;font-family:"Questrial",sans-serif;color:var(--blue-deep)}
.section-title{font-weight:400;font-size:25px}
.intro p{font-size:11px;line-height:16.5px;width:570px;margin:6px auto 0}
.services{position:absolute;top:509px;left:0;width:882px;height:200px;background:var(--band);display:flex;justify-content:center;gap:54px;padding-top:17px;color:var(--white);text-align:center}
.service{width:170px;font-family:"Questrial",sans-serif}
.service-icon{width:48px;height:48px;margin:0 auto;border-radius:7px;background:linear-gradient(#2a86d8,#1668b8);box-shadow:0 2px 3px rgba(0,0,0,.2);display:flex;align-items:center;justify-content:center}
.service h3{font-family:"Open Sans",sans-serif;font-weight:600;font-size:10px;line-height:13px;margin:12px 0 12px;min-height:14px}
.service p{font-size:8px;line-height:12px}
.clients{position:absolute;top:739px;left:0;width:882px;text-align:center;font-family:"Questrial",sans-serif;color:var(--blue-deep)}
.clients p{font-size:11px;line-height:17px;width:570px;margin:4px auto 0}
.testimonials{position:absolute;top:823px;left:179px;display:flex;gap:22px}
.testimonial{width:252px}
.quote-box{position:relative;height:81px;border:1px solid var(--line);border-radius:3px;padding:12px 14px 0 36px;font-size:8.5px;line-height:14px;color:var(--ink);background:var(--white)}
.quote-mark{position:absolute;left:13px;top:4px;font-family:Georgia,serif;font-size:32px;color:#d8dcdf}
.quote-box::after{content:"";position:absolute;left:22px;bottom:-7px;width:12px;height:12px;background:var(--white);border-right:1px solid var(--line);border-bottom:1px solid var(--line);transform:rotate(45deg)}
.author{display:flex;align-items:center;margin:12px 0 0 7px}
.avatar{width:44px;height:44px;border-radius:50%;background:radial-gradient(circle at 50% 40%,#d9d4cf,#8e9aa6);border:2px solid var(--white);box-shadow:0 0 0 1px var(--line)}
.author-info{margin-left:7px;font-family:"Questrial",sans-serif;font-size:10px;line-height:15px}
.author-name{color:var(--blue)}
.author-role{color:var(--muted)}
.site-footer{position:absolute;top:1007px;left:0;width:882px;height:151px;background:var(--footer);padding:27px 0 0 147px;display:flex}
.foot-col h4{color:var(--white);font-size:9.5px;font-weight:600;margin-bottom:7px}
.foot-col li{list-style:none;color:var(--footer-text);font-size:7.5px;line-height:13px}
.col-links{width:93px}.col-about{width:129px}.col-community{width:129px}
.newsletter p{color:var(--footer-text);font-size:7.5px;margin-bottom:6px}
.subscribe{display:flex;gap:3px}
.email{width:209px;height:26px;background:var(--white);border-radius:2px;font-size:8px;color:#333;line-height:26px;padding-left:8px;display:flex;align-items:center;gap:5px}
.ok{width:28px;height:26px;background:var(--blue);color:var(--white);font-weight:700;font-size:9.5px;line-height:26px;text-align:center;border-radius:2px}
.bottom-bar{position:absolute;top:1158px;left:0;width:882px;height:42px;background:var(--white);font-size:7px;color:var(--ink);padding:15px 0 0 147px}
.social{position:absolute;right:146px;top:11px;display:flex;gap:3px}
.social span{width:16px;height:16px;border-radius:50%;background:var(--blue)}
</style>
</head>
<body>
<div class="topbar"><span class="dot"></span>Posted by @loremipsum 15 minutes ago: <b>Quisque porttitor interdum libero vel sociosqu ad litora</b></div>

<header class="site-nav">
  <nav class="menu">
    <span>Home</span><span>Our Services</span><span>Partners &amp; Clients</span><span>About Us</span><span>Contact Us</span>
    <span class="btn-sm btn-signup">SignUp Now!</span>
    <span class="btn-sm btn-login">&#128274; Login</span>
  </nav>
</header>

<section class="hero">
  <div class="hero-photo" role="img" aria-label="Blurred photo of business people meeting around a conference table"></div>
  <div class="hero-copy">
    <h1>Creating Success Cases</h1>
    <p>“Getting into a new market is easier than staying in that market.”</p>
  </div>
  <div class="cta">Click here and Get Started</div>
  <svg class="arrow" style="left:22px" width="18" height="30" viewBox="0 0 18 30"><path d="M15 2 L3 15 L15 28" fill="none" stroke="#111" stroke-width="4"/></svg>
  <svg class="arrow" style="right:22px" width="18" height="30" viewBox="0 0 18 30"><path d="M3 2 L15 15 L3 28" fill="none" stroke="#111" stroke-width="4"/></svg>
  <svg class="hero-edge" width="882" height="60" viewBox="0 0 882 60">
    <path d="M0 6 Q200 14 400 14 L472 46 L466 14 Q700 10 882 0 L882 60 L0 60Z" fill="#e4e9ec"/>
    <path d="M0 10 Q200 18 400 20 L472 52 L466 20 Q700 16 882 8 L882 60 L0 60Z" fill="#fff"/>
  </svg>
</section>

<section class="intro">
  <h2 class="section-title">Why all Clients Love our Solution?</h2>
  <p>The world is fast becoming a global economy and businesses wanting to succeed in this highly competitive environment must have access to up to date business informat Halvenor Associates is an internationally focused business facilitator headquartered in Harbor Point, Oregon.</p>
</section>

<section class="services">
  <div class="service">
    <div class="service-icon"><svg width="26" height="26" viewBox="0 0 26 26"><circle cx="13" cy="17" r="6" fill="none" stroke="#fff" stroke-width="3"/><path d="M6 3 L11 11 M20 3 L15 11" stroke="#fff" stroke-width="3"/></svg></div>
    <h3>Market Matching</h3>
    <p>* Research Appropriate Firms<br>* Present Your Product/Service<br>* Select Potential Matches<br>* Introduce You to Companies Specifically Interested in Your Product/Service</p>
  </div>
  <div class="service">
    <div class="service-icon"><svg width="24" height="26" viewBox="0 0 24 26"><rect x="3" y="2" width="18" height="22" rx="2" fill="#fff"/><path d="M7 8h10M7 12h10M7 16h10M7 20h7" stroke="#1a6fb8" stroke-width="1.5"/></svg></div>
    <h3>List Services</h3>
    <p>Fast and Accurate Lists of Importers, Agents, Distributors, Manufacturers, Joint Venture Partners, Manufacturing Under License Partners, Investment Partners.</p>
  </div>
  <div class="service">
    <div class="service-icon"><svg width="26" height="26" viewBox="0 0 26 26"><path d="M3 3h20v15H12l-5 5v-5H3z" fill="#fff"/><path d="M13 6v7M13 15v2" stroke="#1a6fb8" stroke-width="2.5"/></svg></div>
    <h3>Industry Alert and Market Overviews</h3>
    <p>Track and report industry news,emerging trends, mergers, and acquisitions which affect your industry/product AND Overviews of Overview of the Industry/Product, Competitive Environment</p>
  </div>
</section>

<section class="clients">
  <h2 class="section-title">The Best Solution... The Happiest Clients</h2>
  <p>With over 15 years of experience in international business information services, Halvenor Associates has assisted a broad range of companies to enter the international marketplace</p>
</section>

<div class="testimonials">
  <article class="testimonial">
    <div class="quote-box"><span class="quote-mark">“</span>Lorem Ipsum is simply dummy text of the printing and typesetting industry. Lorem Ipsum has been the industry's standard dummy text ever since the 1500s, when an unknown printer took.</div>
    <div class="author"><div class="avatar" role="img" aria-label="Client portrait photo"></div><div class="author-info"><div class="author-name">Martin Okafor Lindqvist</div><div class="author-role">Brightmoor Labs, Founder CEO</div></div></div>
  </article>
  <article class="testimonial">
    <div class="quote-box"><span class="quote-mark">“</span>Lorem Ipsum is simply dummy text of the printing and typesetting industry. Lorem Ipsum has been the industry's standard dummy text ever since the 1500s, when an unknown printer took.</div>
    <div class="author"><div class="avatar" role="img" aria-label="Client portrait photo"></div><div class="author-info"><div class="author-name">Martin Okafor Lindqvist</div><div class="author-role">Brightmoor Labs, Founder CEO</div></div></div>
  </article>
</div>

<footer class="site-footer">
  <div class="foot-col col-links"><h4>Quick Links</h4><ul><li>Home</li><li>Our Solution</li><li>Partners &amp; Clients</li><li>About Us</li><li>Client Testimonials</li><li>Contact Us</li></ul></div>
  <div class="foot-col col-about"><h4>About Us</h4><ul><li>Company Profile</li><li>Careers</li><li>Corporate Partnerships</li><li>Frequently Asked Questions</li><li>Clients</li></ul></div>
  <div class="foot-col col-community"><h4>Community</h4><ul><li>Download our Freee API</li><li>SignUp Now</li><li>My First Project</li></ul></div>
  <div class="foot-col newsletter"><h4>Subscribe to our Newsletter</h4><p>Subscribe to new Solutions, Services and Stuff.</p>
    <div class="subscribe"><div class="email"><svg width="10" height="7" viewBox="0 0 10 7"><rect width="10" height="7" fill="#222"/><path d="M0 0 L5 4 L10 0" fill="none" stroke="#fff" stroke-width="1"/></svg>Email Address</div><div class="ok">OK</div></div>
  </div>
</footer>

<div class="bottom-bar">Copyright © 2013 - Halvenor Associates - All Rights Reserved.
  <div class="social"><span></span><span></span><span></span><span></span></div>
</div>
</body>
</html>
```